Trade Show Display Design For A Real Estate Lending Company

We are in need of an impactful and modern trade show booth design that is consistent with the new branding and imagery found on our website www.kvr7.net.

Established in 2010, Torvale Crest Funding, LLC is a Hard Money Lender providing fast bridge financing to real estate investors for the purchase, renovation, or new construction of single family, multi-family and mixed use properties. We have closed over 800 loans since we began with total transaction amounts in excess of $170 million.

We like to stress that we are local lenders, and our lending area includes NJ, NY, CT, MA, PA, FL, MD, VA, DC. In addition, one of our major differentiators is that we close loans extremely fast.
Here is what we need for this project, and the artwork templates are attached.

-1 backdrop display design
-1 countertop wrap design
-1 retractable banner design

The backdrop display and the countertop will be used together. The retractable banner will be used together with the backdrop and by itself.

Target Market(s)

Real estate agents, mortgage brokers, builders, and other real estate investors.

Industry/Entity Type

Real Estate

Font styles to use
Other font styles liked:
• Proxima Nova and Roboto Slab (or similar)

Requirements
Must have
• Must include a design for all three elements (backdrop, retractable banner, counter top). Final submission must also be submitted using the print-ready art templates provided.

```html
<!DOCTYPE html>
<html lang="en">
<head>
<meta charset="utf-8">
<title>Torvale Crest Funding – Trade Show Set</title>
<link href="https://fonts.googleapis.com/css2?family=Montserrat:wght@400;500;600&display=swap" rel="stylesheet">
<style>
:root{
  --bg:#e4e4e4;
  --teal-dark:#0c4553;
  --teal:#135a68;
  --teal-light:#1d6b79;
  --brand-green:#4d8b78;
  --white:#ffffff;
  --line:#d6e6ea;
  --accent:#e68a1c;
  --photo-a:#8a6f62;
  --photo-b:#5a5d63;
}
*{box-sizing:border-box;margin:0;padding:0}
html,body{width:1200px;height:897px;overflow:hidden;background:var(--bg);font-family:"Montserrat",sans-serif;color:var(--white)}
.stage{position:relative;width:1200px;height:897px}
.panel{position:absolute;background:linear-gradient(160deg,var(--teal-light),var(--teal) 45%,var(--teal-dark));overflow:hidden}
.photo{background:linear-gradient(135deg,var(--photo-a),#9b7b6b 40%,var(--photo-b))}
.brand-block{background:var(--brand-green);display:flex;align-items:center;gap:10px}
.brand-square{width:18px;height:18px;border:2px solid var(--white);flex:none}
.brand-name{font-weight:500;line-height:1.25;text-transform:uppercase;letter-spacing:.04em}
.features{display:grid;grid-template-columns:1fr 1fr}
.feature{display:flex;align-items:center;gap:8px}
.feature svg{flex:none}
.contact{color:var(--accent);display:flex;align-items:center}

/* retractable banner */
.banner{left:40px;top:150px;width:210px;height:570px}
.banner .head{display:flex;align-items:center;gap:8px;padding:26px 0 0}
.banner .brand-block{width:82px;height:36px;padding:0 6px;gap:5px}
.banner .brand-square{width:9px;height:9px;border-width:1px}
.banner .brand-name{font-size:5px}
.banner .tagline{font-size:7px;line-height:1.3}
.banner .deliver{font-size:8.5px;text-align:center;margin:20px 0 12px}
.banner .features{padding:0 20px;row-gap:17px;font-size:7px;column-gap:6px}
.banner .feature{gap:6px}
.banner .photo{position:absolute;left:0;top:222px;width:210px;height:110px}
.banner .states-title{position:absolute;top:350px;width:100%;text-align:center;font-size:8px;line-height:1.4}
.banner .states{position:absolute;top:392px;left:28px;right:28px;display:grid;grid-template-columns:1fr 1fr;gap:8px 8px}
.state{border:1px solid var(--line);font-size:5px;text-align:center;padding:3px 0;letter-spacing:.05em}
.banner .contact{position:absolute;top:505px;left:0;right:0;justify-content:center;font-size:8.5px;gap:12px}
.divider{width:1px;height:26px;background:var(--accent)}

/* backdrop */
.backdrop{left:275px;top:150px;width:640px;height:500px}
.backdrop .brand-block{position:absolute;left:44px;top:40px;width:170px;height:88px;padding:0 18px}
.backdrop .brand-name{font-size:10px}
.backdrop .tagline{position:absolute;left:250px;top:74px;font-size:17px;font-weight:500}
.backdrop .photo{position:absolute;left:44px;top:190px;width:400px;height:230px}
.backdrop .features{position:absolute;left:462px;top:210px;width:170px;row-gap:68px;column-gap:10px;font-size:8.5px}

/* counter */
.counter{left:935px;top:330px;width:225px;height:320px;border-top:8px solid #1b1b1b}
.counter .brand-block{background:none;position:absolute;left:22px;top:80px;gap:12px}
.counter .brand-square{width:26px;height:26px}
.counter .brand-name{font-size:13px}
.counter .contact{position:absolute;top:200px;left:0;right:0;justify-content:center;font-size:8px;gap:6px}
</style>
</head>
<body>
<div class="stage">

  <!-- Retractable banner -->
  <section class="panel banner">
    <div class="head">
      <div class="brand-block"><span class="brand-square"></span><span class="brand-name">Torvale Crest<br>Funding, LLC</span></div>
      <p class="tagline">Your Fastest Local Source<br>for Hard Money.</p>
    </div>
    <p class="deliver">We Deliver:</p>
    <div class="features">
      <div class="feature"><svg width="10" height="10" viewBox="0 0 10 10"><circle cx="5" cy="5" r="4.3" fill="none" stroke="#fff" stroke-width=".8"/><text x="5" y="7" font-size="6" text-anchor="middle" fill="#fff">$</text></svg>Hard Money</div>
      <div class="feature"><svg width="10" height="10" viewBox="0 0 10 10"><circle cx="5" cy="5" r="4.3" fill="none" stroke="#fff" stroke-width=".8"/><path d="M5 2.5V5l2 1" stroke="#fff" stroke-width=".8" fill="none"/></svg>Fast Processing</div>
      <div class="feature"><svg width="10" height="10" viewBox="0 0 10 10"><circle cx="5" cy="5" r="4.3" fill="none" stroke="#fff" stroke-width=".8"/><path d="M.7 5h8.6M5 .7c-2 2.5-2 6 0 8.6M5 .7c2 2.5 2 6 0 8.6" stroke="#fff" stroke-width=".6" fill="none"/></svg>Local Services</div>
      <div class="feature"><svg width="10" height="10" viewBox="0 0 10 10"><rect x="1" y="2" width="6" height="4" rx="1.5" fill="none" stroke="#fff" stroke-width=".8"/><rect x="3.5" y="4.5" width="5.5" height="3.5" rx="1.5" fill="none" stroke="#fff" stroke-width=".8"/></svg>Financial Coaching</div>
      <div class="feature"><svg width="10" height="10" viewBox="0 0 10 10"><path d="M1 9h8M2 9V7M4 9V5M6 9V6M8 9V3M1.5 5l2.5-2 2 1.5L9 1.5" stroke="#fff" stroke-width=".8" fill="none"/></svg>Profitability</div>
      <div class="feature"><svg width="10" height="10" viewBox="0 0 10 10"><circle cx="5" cy="5" r="4.3" fill="none" stroke="#fff" stroke-width=".8"/><path d="M3 6c1.2 1.2 2.8 1.2 4 0" stroke="#fff" stroke-width=".8" fill="none"/></svg>Peace of Mind</div>
    </div>
    <div class="photo" role="img" aria-label="Photo of two builders crouching beside a brick wall on a rooftop site"></div>
    <p class="states-title">TCF Lends In<br>The Following States:</p>
    <div class="states">
      <span class="state">CONNECTICUT</span><span class="state">NEW YORK</span>
      <span class="state">MASSACHUSETTS</span><span class="state">PENNSYLVANIA</span>
      <span class="state">MARYLAND</span><span class="state">VIRGINIA &amp; D.C.</span>
      <span class="state">NEW JERSEY</span><span class="state">FLORIDA</span>
    </div>
    <div class="contact"><span>555.014.2290</span><span class="divider"></span><span>info@kvr7.net</span></div>
  </section>

  <!-- Backdrop -->
  <section class="panel backdrop">
    <div class="brand-block"><span class="brand-square"></span><span class="brand-name">Torvale Crest<br>Funding, LLC</span></div>
    <h1 class="tagline">Your Fastest Local Source for Hard Money.</h1>
    <div class="photo" role="img" aria-label="Photo of two builders crouching beside a brick wall on a rooftop site"></div>
    <div class="features">
      <div class="feature"><svg width="13" height="13" viewBox="0 0 10 10"><circle cx="5" cy="5" r="4.3" fill="none" stroke="#fff" stroke-width=".7"/><text x="5" y="7" font-size="6" text-anchor="middle" fill="#fff">$</text></svg>Hard Money</div>
      <div class="feature"><svg width="13" height="13" viewBox="0 0 10 10"><circle cx="5" cy="5" r="4.3" fill="none" stroke="#fff" stroke-width=".7"/><path d="M5 2.5V5l2 1" stroke="#fff" stroke-width=".7" fill="none"/></svg>Fast Processing</div>
      <div class="feature"><svg width="13" height="13" viewBox="0 0 10 10"><circle cx="5" cy="5" r="4.3" fill="none" stroke="#fff" stroke-width=".7"/><path d="M.7 5h8.6M5 .7c-2 2.5-2 6 0 8.6M5 .7c2 2.5 2 6 0 8.6" stroke="#fff" stroke-width=".5" fill="none"/></svg>Local Services</div>
      <div class="feature"><svg width="13" height="13" viewBox="0 0 10 10"><rect x="1" y="2" width="6" height="4" rx="1.5" fill="none" stroke="#fff" stroke-width=".7"/><rect x="3.5" y="4.5" width="5.5" height="3.5" rx="1.5" fill="none" stroke="#fff" stroke-width=".7"/></svg>Financial Coaching</div>
      <div class="feature"><svg width="13" height="13" viewBox="0 0 10 10"><path d="M1 9h8M2 9V7M4 9V5M6 9V6M8 9V3M1.5 5l2.5-2 2 1.5L9 1.5" stroke="#fff" stroke-width=".7" fill="none"/></svg>Profitability</div>
      <div class="feature"><svg width="13" height="13" viewBox="0 0 10 10"><circle cx="5" cy="5" r="4.3" fill="none" stroke="#fff" stroke-width=".7"/><path d="M3 6c1.2 1.2 2.8 1.2 4 0" stroke="#fff" stroke-width=".7" fill="none"/></svg>Peace of Mind</div>
    </div>
  </section>

  <!-- Countertop wrap -->
  <section class="panel counter">
    <div class="brand-block"><span class="brand-square"></span><span class="brand-name">Torvale Crest<br>Funding, LLC</span></div>
    <div class="contact"><span>555.014.2290</span><span>|</span><span>info@kvr7.net</span></div>
  </section>

</div>
</body>
</html>
```